Restaurant menu design

I need a menu for a restaurant in Spain.
It has to be bohemian but modern. We need something romantic and elegant.
The restaurant is elegant with good food and an excellent reputation. It is also modern at the same time.
The restaurant is superbly decorated and very chick so we need something "class" to fit in with the surroundings.
The size of the document must be 325 mm in high and 245 mm as a maximum and preferably made in indesign.

Reason: Thank you all for your designs.
So far all your designs are ok but it isn´t what we are looking for. Most of the designs are too loaded, too many colors and too much decoration.

Target Market(s)

Adults of various age groups and different nationalities mostly European.

Industry/Entity Type

Restaurant

Requirements
Must have
• The menu must have two interior pages with the text as in the document attached.It must be easily legible.
Nice to have
• See what kind of menus they use in important restaurants in places like Paris, see what designs are in trend, but Not necessarily doing the same style if it doesn’t fit in with the description above.
Should not have
• Nothing old fashioned.

```html
<!DOCTYPE html>
<html lang="en">
<head>
<meta charset="utf-8">
<title>Le Velours — Menu Cover</title>
<link rel="stylesheet" href="https://fonts.googleapis.com/css2?family=Cormorant+Garamond:wght@500&family=Pinyon+Script&display=swap">
<style>
  :root {
    --rose-ground: #c8a193;
    --rose-deep: #b98f81;
    --rose-light: #d9b8ae;
    --panel-white: #ffffff;
    --ink: #111111;
    --plum: #8e5a7a;
  }
  * { margin: 0; padding: 0; box-sizing: border-box; }
  html, body {
    width: 904px;
    height: 1200px;
    overflow: hidden;
    background: var(--rose-ground);
  }
  .menu-cover {
    position: relative;
    width: 904px;
    height: 1200px;
    background: var(--rose-ground);
    overflow: hidden;
  }
  .illustration-area {
    position: absolute;
    left: 88px;
    top: 70px;
    width: 290px;
    height: 1110px;
    background: linear-gradient(180deg, var(--rose-ground) 0%, var(--rose-deep) 30%, var(--rose-deep) 70%, var(--rose-ground) 100%);
    opacity: 0.7;
  }
  .brand-panel {
    position: absolute;
    left: 425px;
    top: 167px;
    width: 479px;
    height: 482px;
    background: var(--panel-white);
    border-radius: 26px 0 0 26px;
    display: flex;
    align-items: center;
    justify-content: center;
    gap: 14px;
  }
  .brand-mark {
    width: 16px;
    height: 16px;
    border-radius: 50%;
    background: var(--plum);
  }
  .brand-name {
    font-family: "Cormorant Garamond", Georgia, serif;
    font-weight: 500;
    font-size: 76px;
    line-height: 1;
    color: var(--ink);
    letter-spacing: 1px;
  }
  .cover-title {
    position: absolute;
    left: 516px;
    top: 860px;
    font-family: "Pinyon Script", cursive;
    font-weight: 400;
    font-size: 138px;
    line-height: 1;
    color: var(--panel-white);
  }
</style>
</head>
<body>
  <main class="menu-cover">
    <div class="illustration-area" role="img" aria-label="Tall stylised illustration of an elegant figure in a long flowing evening gown"></div>

    <section class="brand-panel">
      <span class="brand-mark" aria-hidden="true"></span>
      <h1 class="brand-name">Le Velours</h1>
    </section>

    <p class="cover-title">Menu</p>
  </main>
</body>
</html>
```